Commercial Real Estate website

Need a web design commercial real estate company specializing in retail shopping centers based in Orlando, FL. We would like pictures of Orlando city skyline with hues and colors that go with hot pink. We want to stress the relationship of time on the value of real estate.
It should gave a rotating page that highlights our property listings.

Target Market(s)

Owners of shopping centers and national retail tenants looking for tenant representatives.

Industry/Entity Type

Real Estate

Number of Pages Required

5+ page

Font styles to use
Serif

Colors
e34197

Requirements
Must have
• Pictures of commercial retail grocery anchored shopping centers and city scapes and skylines.

```html
<!DOCTYPE html>
<html lang="en">
<head>
<meta charset="utf-8">
<title>Hourglass Commercial – Retail Real Estate</title>
<link href="https://fonts.googleapis.com/css2?family=PT+Serif:wght@400;700&family=Open+Sans:wght@400;600;700&display=swap" rel="stylesheet">
<style>
:root{
  --pink:#e34197;
  --pink-dark:#c12c7b;
  --ink:#333333;
  --muted:#777777;
  --page-bg:#e6e6e6;
  --panel:#f3f3f3;
  --footer:#2b2b2b;
  --footer-deep:#1d1d1d;
  --line:#d8d8d8;
  --white:#ffffff;
}
*{box-sizing:border-box;margin:0;padding:0}
html,body{width:786px;height:1200px;overflow:hidden}
body{background:var(--page-bg);font-family:"Open Sans",Arial,sans-serif;color:var(--ink);font-size:7px;line-height:1.45}
ul{list-style:none}
.page{width:600px;margin:0 auto;background:var(--white);height:1035px;position:relative}

/* header */
.site-header{height:73px;display:flex;justify-content:space-between;align-items:center;padding:0 22px}
.brand{display:flex;align-items:center;gap:8px}
.brand-dot{width:26px;height:26px;border-radius:50%;background:var(--pink)}
.brand-name{font-family:"PT Serif",Georgia,serif;font-size:22px;color:var(--pink);font-weight:700}
.header-tools{text-align:right}
.top-links{display:flex;gap:12px;justify-content:flex-end;font-size:7px;color:var(--muted)}
.phone{display:flex;align-items:center;gap:6px;justify-content:flex-end;margin:4px 0;font-size:18px;font-weight:700;color:var(--pink)}
.search{display:flex;justify-content:flex-end}
.search-field{width:120px;height:14px;border:1px solid var(--line)}
.search-btn{height:14px;background:#333;color:var(--white);font-size:6px;padding:0 8px;line-height:14px;font-weight:700}

/* nav */
.main-nav{margin:0 12px;height:26px;background:linear-gradient(var(--pink),var(--pink-dark));display:flex;border-radius:2px}
.main-nav a{flex:1;text-align:center;color:var(--white);font-size:7px;font-weight:700;line-height:26px;text-decoration:none;border-right:1px solid rgba(255,255,255,.3)}
.main-nav a:last-child{border-right:0}
.main-nav a.is-active{background:rgba(255,255,255,.18)}

/* hero */
.hero{position:relative;margin:10px 0 0;height:236px}
.hero-photo{position:absolute;inset:0;background:linear-gradient(180deg,#2a3b5c 0%,#46567a 35%,#8a6a58 68%,#d9934e 82%,#3a3030 100%)}
.hero-caption{position:absolute;left:0;right:0;bottom:14px;background:rgba(0,0,0,.55);padding:8px 40px;color:var(--white)}
.hero-caption h2{font-size:13px;font-weight:700;letter-spacing:.3px}
.hero-caption p{font-size:6.5px;color:#ddd}
.hero-arrow{position:absolute;top:104px;width:24px;height:24px;border-radius:50%;background:rgba(60,60,60,.75)}
.hero-arrow.prev{left:-12px}.hero-arrow.next{right:-12px}
.hero-arrow svg{display:block;margin:6px auto}

/* welcome */
.welcome{margin:18px 22px 0;background:var(--panel);border-left:4px solid var(--pink);padding:12px 16px;height:96px;position:relative;box-shadow:0 2px 4px rgba(0,0,0,.12)}
.welcome h1{font-family:"PT Serif",Georgia,serif;font-size:17px;font-weight:400;color:#444}
.welcome h1 span{color:var(--pink)}
.welcome p{margin-top:5px;width:420px;color:var(--muted)}
.btn{display:inline-block;background:var(--pink);color:var(--white);font-size:6.5px;font-weight:700;padding:3px 12px;border-radius:9px}
.welcome .btn{position:absolute;right:18px;bottom:12px}

/* services */
.services{display:flex;gap:16px;padding:20px 36px 0;height:212px}
.service{flex:1;background:var(--panel);text-align:center;position:relative;padding-bottom:8px}
.service-title{background:var(--pink);color:var(--white);font-family:"PT Serif",Georgia,serif;font-size:8.5px;font-weight:700;padding:5px 0;margin:-6px -6px 0;text-transform:uppercase}
.service-photo{height:70px;margin:8px;background:linear-gradient(135deg,#c9ced6,#8e98a8)}
.service p{font-size:6px;color:var(--muted);padding:0 10px;text-align:left;height:40px}

/* listings */
.listings{padding:10px 22px 0}
.section-title{display:flex;align-items:center;gap:12px;font-family:"PT Serif",Georgia,serif;font-size:17px;color:#444}
.section-title::before,.section-title::after{content:"";flex:1;height:1px;background:var(--line)}
.listing-tabs{display:flex;justify-content:space-around;font-family:"PT Serif",Georgia,serif;font-size:9px;color:#555;margin:6px 0 6px}
.cards{display:flex;gap:12px}
.card{flex:1;border:1px solid var(--line);padding:6px;height:168px;box-shadow:0 1px 3px rgba(0,0,0,.1)}
.card-photo{height:70px;background:linear-gradient(180deg,#b9d2e6 0%,#dfe7ec 45%,#a88a6a 60%,#7c8a5c 100%)}
.card h3{font-size:6.5px;font-weight:700;margin:5px 0 3px;text-transform:uppercase}
.card p{font-size:6px;color:var(--muted)}
.card .price{color:var(--pink);font-weight:700;margin-top:3px}
.card .btn{margin-top:6px}

/* partners */
.partners{display:flex;justify-content:space-around;align-items:center;padding:18px 40px 0}
.partner{background:#cfcfcf}

/* footer */
.site-footer{position:absolute;left:0;top:1035px;width:786px;height:165px;background:var(--footer);color:#bbb}
.footer-inner{width:600px;margin:0 auto;display:flex;gap:22px;padding:12px 22px 0;height:145px;position:relative}
.footer-col h4{color:var(--white);font-size:8px;font-weight:700;margin-bottom:5px}
.footer-col li{font-size:6.5px;line-height:1.55}
.col-menu{width:70px}.col-links{width:80px}.col-about{width:170px}.col-contact{flex:1}
.about-row{display:flex;gap:6px}
.about-photo{width:62px;height:40px;background:linear-gradient(135deg,#6b6b6b,#9a9a9a);flex:none}
.about-row p{font-size:6px}
.contact-line{display:flex;gap:5px;align-items:center;font-size:6.5px;margin-bottom:3px}
.social{display:flex;gap:4px;margin-top:4px}
.social span{width:11px;height:11px;border-radius:50%;background:#555}
.newsletter{position:absolute;left:196px;top:104px;display:flex;align-items:center;gap:6px}
.newsletter h4{color:var(--white);font-size:8px}
.newsletter-field{width:120px;height:14px;background:var(--white)}
.newsletter .btn{border-radius:0;padding:3px 10px}
.copyright{height:20px;background:var(--footer-deep);text-align:center;line-height:20px;font-size:6.5px;color:#999}
</style>
</head>
<body>
<div class="page">
  <header class="site-header">
    <div class="brand">
      <span class="brand-dot"></span>
      <span class="brand-name">Hourglass Commercial</span>
    </div>
    <div class="header-tools">
      <ul class="top-links"><li>Sign In</li><li>Register</li><li>Resources</li><li>Contact Us</li></ul>
      <div class="phone">
        <svg width="14" height="14" viewBox="0 0 24 24"><path fill="#e34197" d="M6.6 10.8a15 15 0 0 0 6.6 6.6l2.2-2.2c.3-.3.7-.4 1-.2 1.1.4 2.3.6 3.6.6.6 0 1 .4 1 1V20c0 .6-.4 1-1 1A17 17 0 0 1 3 4c0-.6.4-1 1-1h3.5c.6 0 1 .4 1 1 0 1.3.2 2.5.6 3.6.1.3 0 .7-.2 1z"/></svg>
        (555) - 0142 - 7730
      </div>
      <div class="search"><span class="search-field"></span><span class="search-btn">SEARCH</span></div>
    </div>
  </header>

  <nav class="main-nav">
    <a class="is-active">HOME</a><a>ABOUT US</a><a>SERVICES</a><a>FEATURED LISTINGS</a><a>PORTFOLIO</a><a>BLOG</a><a>MEDIA</a><a>CONTACT US</a>
  </nav>

  <section class="hero">
    <div class="hero-photo" role="img" aria-label="Orlando city skyline at dusk with lit towers"></div>
    <div class="hero-caption">
      <h2>LOREM IPSUM DOLOR SIT AMET CONSECTETEUR ADIPISCING ELIT</h2>
      <p>Retail centers grow in value over time. We guide owners and national tenants through every lease, sale and renewal across Central Florida.</p>
    </div>
    <span class="hero-arrow prev"><svg width="12" height="12" viewBox="0 0 12 12"><path d="M8 2 4 6l4 4" stroke="#fff" stroke-width="2" fill="none"/></svg></span>
    <span class="hero-arrow next"><svg width="12" height="12" viewBox="0 0 12 12"><path d="M4 2l4 4-4 4" stroke="#fff" stroke-width="2" fill="none"/></svg></span>
  </section>

  <section class="welcome">
    <h1>WELCOME TO <span>Hourglasscommercial.com</span></h1>
    <p>We represent owners of grocery anchored shopping centers and national retail tenants. Our team tracks every market cycle so that timing works in your favor, whether you are leasing new space, selling a center or planning the next location for your brand in Orlando and beyond.</p>
    <span class="btn">Read more</span>
  </section>

  <section class="services">
    <article class="service">
      <h3 class="service-title">Projects Management</h3>
      <div class="service-photo" role="img" aria-label="Project team reviewing plans"></div>
      <p>From site selection to grand opening, we keep each retail project on schedule and on budget.</p>
      <span class="btn">Read more</span>
    </article>
    <article class="service">
      <h3 class="service-title">The Portfolio</h3>
      <div class="service-photo" role="img" aria-label="Shopping center portfolio meeting"></div>
      <p>Browse anchored centers we have leased, sold and managed for owners across the region.</p>
      <span class="btn">Read more</span>
    </article>
    <article class="service">
      <h3 class="service-title">Future Projects</h3>
      <div class="service-photo" role="img" aria-label="New retail development planning"></div>
      <p>See upcoming developments and early leasing chances for national retail tenants.</p>
      <span class="btn">Read more</span>
    </article>
  </section>

  <section class="listings">
    <h2 class="section-title">FEATURED LISTINGS</h2>
    <div class="listing-tabs"><span>FOR LEASE</span><span>FOR SALE</span></div>
    <div class="cards">
      <article class="card">
        <div class="card-photo" role="img" aria-label="Grocery anchored shopping center"></div>
        <h3>Lake Nona Market Plaza</h3>
        <p>1200 Market Way, Orlando, FL</p><p>Size: 24,500 SF</p><p class="price">$18.00 / SF</p>
        <span class="btn">Read more</span>
      </article>
      <article class="card">
        <div class="card-photo" role="img" aria-label="Retail strip center storefronts"></div>
        <h3>Colonial Square Center</h3>
        <p>455 Colonial Dr, Orlando, FL</p><p>Size: 12,800 SF</p><p class="price">$22.50 / SF</p>
        <span class="btn">Read more</span>
      </article>
      <article class="card">
        <div class="card-photo" role="img" aria-label="Neighborhood shopping center"></div>
        <h3>Winter Park Commons</h3>
        <p>88 Park Ave, Winter Park, FL</p><p>Size: 41,000 SF</p><p class="price">$6,400,000</p>
        <span class="btn">Read more</span>
      </article>
      <article class="card">
        <div class="card-photo" role="img" aria-label="Anchored retail center parking lot"></div>
        <h3>Kissimmee Town Center</h3>
        <p>310 Vine St, Kissimmee, FL</p><p>Size: 56,200 SF</p><p class="price">$9,150,000</p>
        <span class="btn">Read more</span>
      </article>
    </div>
  </section>

  <section class="partners" aria-label="Partners">
    <span class="partner" style="width:90px;height:22px"></span>
    <span class="partner" style="width:34px;height:34px;border-radius:50%"></span>
    <span class="partner" style="width:96px;height:26px"></span>
    <span class="partner" style="width:100px;height:20px"></span>
  </section>
</div>

<footer class="site-footer">
  <div class="footer-inner">
    <div class="footer-col col-menu">
      <h4>Main Menu</h4>
      <ul><li>Home</li><li>About Us</li><li>Services</li><li>Featured Listings</li><li>Portfolio</li><li>Blog</li><li>Media</li><li>Contact Us</li></ul>
    </div>
    <div class="footer-col col-links">
      <h4>Useful links</h4>
      <ul><li>Sitemap</li><li>Help</li><li>Privacy Policy</li><li>Testimonials</li><li>News &amp; Updates</li></ul>
    </div>
    <div class="footer-col col-about">
      <h4>ABOUT US</h4>
      <div class="about-row">
        <div class="about-photo" role="img" aria-label="Brokerage team"></div>
        <p>A Central Florida team focused on retail centers, tenant representation and long term value.</p>
      </div>
    </div>
    <div class="footer-col col-contact">
      <h4>GET IN TOUCH</h4>
      <div class="contact-line"><svg width="8" height="8" viewBox="0 0 24 24"><path fill="#e34197" d="M12 2a7 7 0 0 0-7 7c0 5 7 13 7 13s7-8 7-13a7 7 0 0 0-7-7zm0 9.5a2.5 2.5 0 1 1 0-5 2.5 2.5 0 0 1 0 5z"/></svg>200 Orange Ave, Orlando, FL</div>
      <div class="contact-line"><svg width="8" height="8" viewBox="0 0 24 24"><path fill="#e34197" d="M6.6 10.8a15 15 0 0 0 6.6 6.6l2.2-2.2c.3-.3.7-.4 1-.2 1.1.4 2.3.6 3.6.6.6 0 1 .4 1 1V20c0 .6-.4 1-1 1A17 17 0 0 1 3 4c0-.6.4-1 1-1h3.5c.6 0 1 .4 1 1 0 1.3.2 2.5.6 3.6.1.3 0 .7-.2 1z"/></svg>Phone: (555) 0142 7730</div>
      <div class="contact-line"><svg width="8" height="8" viewBox="0 0 24 24"><path fill="#e34197" d="M2 5h20v14H2zm2 2v.5l8 5 8-5V7z"/></svg>hello@hourglasscommercial.com</div>
      <h4 style="margin-top:6px">FOLLOW US</h4>
      <div class="social"><span></span><span></span><span></span><span></span></div>
    </div>
    <div class="newsletter">
      <h4>NEWSLETTER</h4>
      <span class="newsletter-field"></span>
      <span class="btn">SUBMIT</span>
    </div>
  </div>
  <div class="copyright">Copyright © 2024 Hourglasscommercial.com. All rights reserved.</div>
</footer>
</body>
</html>
```